Harrowgate Supply Group Business Card Design

The Business Card will be one side only with Harrowgate Supplies Group Logo
Card should have:
Name
Title
Office phone Number
Cell Number
email address
Website
Street Address
Our Slogan is Rugged and Reliable
Looking for something that stands out from other business cards

Target Market(s)

Heavy equipment Lease Company

```html
<!DOCTYPE html>
<html lang="en">
<head>
<meta charset="utf-8">
<title>Harrowgate Supplies Group – Business Card</title>
<link href="https://fonts.googleapis.com/css2?family=Montserrat:wght@500;600;700&display=swap" rel="stylesheet">
<style>
  :root {
    --backdrop: #8b8d8c;
    --card-light: #ffffff;
    --card-dark: #222222;
    --ink-light: #ffffff;
    --brand-navy: #27296e;
    --brand-red: #e2262c;
    --shadow: rgba(0, 0, 0, 0.35);
  }
  * { margin: 0; padding: 0; box-sizing: border-box; }
  html, body { width: 968px; height: 1200px; overflow: hidden; }
  body {
    position: relative;
    background: var(--backdrop);
    font-family: "Montserrat", Arial, sans-serif;
    color: var(--ink-light);
  }
  .card {
    position: absolute;
    left: 95px;
    width: 801px;
    height: 445px;
    background: var(--card-dark);
    box-shadow: 8px 12px 18px var(--shadow);
  }
  .card--front { top: 99px; }
  .card--alt { top: 659px; }
  .card__brand-band {
    position: absolute;
    left: 0; top: 0;
    width: 100%;
    height: 169px;
    background: var(--card-light);
    display: flex;
    align-items: center;
    justify-content: center;
    gap: 12px;
  }
  .brand-mark {
    width: 22px; height: 22px;
    border-radius: 50%;
    background: var(--brand-red);
  }
  .brand-name {
    font-weight: 700;
    font-size: 25px;
    color: var(--brand-navy);
    letter-spacing: 0.2px;
  }
  .person {
    position: absolute;
    right: 78px;
    text-align: right;
  }
  .card--front .person { top: 187px; }
  .card--alt .person { top: 191px; }
  .person__name {
    font-weight: 600;
    font-size: 38px;
    line-height: 1.1;
  }
  .person__title {
    font-weight: 600;
    font-size: 20px;
    line-height: 1.2;
    margin-top: 2px;
    margin-right: 2px;
  }
  .contact {
    position: absolute;
    left: 68px;
    list-style: none;
    font-weight: 500;
    font-size: 20px;
    line-height: 28.8px;
  }
  .card--front .contact { top: 246px; }
  .card--alt .contact { top: 258px; }
  .contact__label { display: inline-block; }
  .card--alt .contact__label { width: 31px; }
  .website {
    position: absolute;
    left: 0;
    width: 100%;
    padding-left: 142px;
    text-align: center;
    top: 396px;
    font-weight: 500;
    font-size: 20px;
  }
</style>
</head>
<body>

  <section class="card card--front">
    <header class="card__brand-band">
      <span class="brand-mark"></span>
      <span class="brand-name">HARROWGATE SUPPLIES GROUP</span>
    </header>
    <div class="person">
      <p class="person__name">Marla K</p>
      <p class="person__title">Manager</p>
    </div>
    <ul class="contact">
      <li><span class="contact__label">T:</span> 041.556.218</li>
      <li><span class="contact__label">C:</span> 310.555.014</li>
      <li><span class="contact__label">A:</span> 48 Ridge Rd</li>
      <li><span class="contact__label">E:</span> hello@harrowgatesupply.com</li>
    </ul>
    <p class="website">www.harrowgatesupply.com</p>
  </section>

  <section class="card card--alt">
    <header class="card__brand-band">
      <span class="brand-mark"></span>
      <span class="brand-name">HARROWGATE SUPPLIES GROUP</span>
    </header>
    <div class="person">
      <p class="person__name">Marla K</p>
      <p class="person__title">Manager</p>
    </div>
    <ul class="contact">
      <li><span class="contact__label">T:</span> 041.556.218</li>
      <li><span class="contact__label">C:</span> 310.555.014</li>
      <li><span class="contact__label">A:</span> 48 Ridge Rd</li>
      <li><span class="contact__label">E:</span> hello@harrowgatesupply.com</li>
      <li><span class="contact__label">W:</span> www.harrowgatesupply.com</li>
    </ul>
  </section>

</body>
</html>
```